Attention grabbing 6x9 postcard

We are looking to have an attention grabbing post card that be sent out to homeowners from our roofing company Olum Roofing. the concept is that on the front it will say something like (STOP THE KNOCKING!
Tired of roofers knocking on your door? Contact us because we value your time as much as you value the roof over your head."
Olum Roofing
OlumRoofing.com
877.612.OLUM
info@olumroofing.com

Please feel free to come up with something very creative. Once we pick the final design we will provide the copy.

```html
<!DOCTYPE html>
<html lang="en">
<head>
<meta charset="utf-8">
<title>Olum Roofing Postcard</title>
<link rel="stylesheet" href="https://fonts.googleapis.com/css2?family=Fira+Sans+Extra+Condensed:wght@300;400;600;800&family=Montserrat:wght@600&display=swap">
<style>
  :root {
    --ink: #1e1e20;
    --gold: #e8b437;
    --page: #e9e6e1;
    --sky-top: #9cc3e6;
    --timber: #e3d7c3;
    --tile: #d8525c;
    --tile-dark: #b93c48;
  }
  * { box-sizing: border-box; margin: 0; padding: 0; }
  html, body { width: 1200px; height: 1200px; overflow: hidden; background: var(--page); }
  .sheet { position: relative; width: 1200px; height: 1200px; }
  .card-frame {
    position: absolute; left: 180px; width: 840px; height: 560px; overflow: hidden;
    box-shadow: 0 6px 18px rgba(0,0,0,.18);
  }
  .card-frame.front { top: 30px; }
  .card-frame.back { top: 610px; }
  .card {
    position: absolute; left: 0; top: 0; width: 895px; height: 596px;
    transform: scale(0.9385); transform-origin: 0 0;
    background: var(--ink);
    font-family: "Fira Sans Extra Condensed", "Arial Narrow", sans-serif;
    color: var(--gold);
  }
  .card svg.shapes { position: absolute; inset: 0; width: 895px; height: 596px; }
  .brand {
    position: absolute; font-family: "Montserrat", sans-serif; font-weight: 600;
    font-size: 13px; letter-spacing: 2.6px; color: var(--gold); text-align: center; white-space: nowrap;
  }
  .front .brand { right: 36px; top: 116px; }
  .headline {
    position: absolute; right: 36px; top: 320px; text-align: right;
    font-weight: 800; font-size: 66px; line-height: 56px; color: var(--ink); letter-spacing: -0.5px;
  }
  .headline .big { font-size: 66px; }
  .blurb {
    position: absolute; right: 36px; top: 505px; width: 300px; text-align: justify; text-align-last: right;
    font-weight: 400; font-size: 14.5px; line-height: 18px; color: var(--ink);
  }
  .contact-row {
    position: absolute; left: 38px; top: 538px; display: flex; gap: 16px;
    font-size: 16px; font-weight: 400; color: var(--gold);
  }
  .contact-row span::before {
    content: ""; display: inline-block; width: 8px; height: 8px; border: 1.6px solid var(--gold);
    border-radius: 50%; margin-right: 5px; vertical-align: 1px;
  }
  .why {
    position: absolute; right: 407px; top: 36px; text-align: right;
    font-weight: 800; font-size: 44px; line-height: 40px; color: var(--gold);
  }
  .benefits { position: absolute; left: 36px; top: 350px; list-style: none; }
  .benefits li {
    display: flex; align-items: center; height: 54px; font-size: 15px; font-weight: 300; letter-spacing: .2px;
  }
  .benefits svg { width: 40px; height: 40px; margin-right: 12px; flex: none; }
  .benefits b { font-weight: 600; margin-right: 4px; }
  .back .brand { left: 540px; width: 160px; top: 102px; font-size: 11px; letter-spacing: 2.2px; }
  .site {
    position: absolute; left: 568px; top: 482px; font-weight: 800; font-size: 40px; line-height: 44px;
  }
  .phone { position: absolute; left: 570px; top: 528px; font-weight: 400; font-size: 29px; }
</style>
</head>
<body>
<main class="sheet">

  <div class="card-frame front">
    <section class="card">
      <svg class="shapes" viewBox="0 0 895 596" aria-hidden="false">
        <defs>
          <linearGradient id="roofPhoto" x1="0" y1="0" x2="0.6" y2="1">
            <stop offset="0" stop-color="var(--sky-top)"/>
            <stop offset="0.3" stop-color="#cfe0ee"/>
            <stop offset="0.4" stop-color="var(--timber)"/>
            <stop offset="0.62" stop-color="#d9c8ae"/>
            <stop offset="0.72" stop-color="var(--tile)"/>
            <stop offset="1" stop-color="var(--tile-dark)"/>
          </linearGradient>
        </defs>
        <polygon class="accent-strip" points="0,0 100,0 100,243 0,295" fill="var(--gold)"/>
        <polygon class="house-panel" points="736,178 895,270 895,596 557,596 512,570 512,303" fill="var(--gold)"/>
        <polygon class="hero-photo" role="img" aria-label="Photo: roofer in hard hat laying red metal tiles over roof battens under a blue sky"
          points="306,38 512,157 512,390 306,508 100,390 100,157" fill="url(#roofPhoto)"/>
      </svg>
      <div class="brand">OLUM ROOFING</div>
      <h1 class="headline">STOP<br>THE<br>KNOCKING!</h1>
      <p class="blurb">TIRED OF ROOFERS KNOCKING ON YOUR DOOR? CONTACT US BECAUSE WE VALUE YOUR TIME AS MUCH AS YOU VALUE THE ROOF OVER YOUR HEAD.</p>
      <div class="contact-row">
        <span>OLUMROOFING.COM</span>
        <span>877.612.OLUM</span>
        <span>INFO@OLUMROOFING.COM</span>
      </div>
    </section>
  </div>

  <div class="card-frame back">
    <section class="card">
      <svg class="shapes" viewBox="0 0 895 596">
        <defs>
          <linearGradient id="drillPhoto" x1="0" y1="0" x2="1" y2="1">
            <stop offset="0" stop-color="#e27a80"/>
            <stop offset="0.5" stop-color="var(--tile)"/>
            <stop offset="1" stop-color="var(--tile-dark)"/>
          </linearGradient>
        </defs>
        <polygon class="detail-photo" role="img" aria-label="Photo: gloved hands driving screws into red metal roofing with a cordless drill"
          points="0,0 311,0 311,235 140,336 0,255" fill="url(#drillPhoto)"/>
        <line class="divider" x1="528" y1="6" x2="528" y2="590" stroke="var(--gold)" stroke-width="4" stroke-linecap="round" stroke-dasharray="0 10"/>
        <rect class="stamp-box" x="733" y="41" width="125" height="150" fill="none" stroke="var(--gold)" stroke-width="1.5"/>
        <g class="address-lines" stroke="var(--gold)" stroke-width="1.2">
          <line x1="570" y1="246" x2="857" y2="246"/>
          <line x1="570" y1="306" x2="857" y2="306"/>
          <line x1="570" y1="364" x2="857" y2="364"/>
          <line x1="570" y1="422" x2="857" y2="422"/>
        </g>
      </svg>
      <h2 class="why">WHY<br>CHOOSE<br>US?</h2>
      <ul class="benefits">
        <li><svg viewBox="0 0 40 40"><path d="M6 20 L16 30 L34 8" fill="none" stroke="var(--gold)" stroke-width="7" stroke-linejoin="round"/></svg><b>DURABLE MATERIALS</b> - BUILT TO LAST IN ANY WEATHER</li>
        <li><svg viewBox="0 0 40 40"><path d="M6 20 L16 30 L34 8" fill="none" stroke="var(--gold)" stroke-width="7" stroke-linejoin="round"/></svg><b>EXPERIENCED TEAM</b> - YEARS OF INDUSTRY EXPERTISE</li>
        <li><svg viewBox="0 0 40 40"><path d="M6 20 L16 30 L34 8" fill="none" stroke="var(--gold)" stroke-width="7" stroke-linejoin="round"/></svg><b>AFFORDABLE PRICING</b> - QUALITY SERVICE AT COMPETITIVE RATES</li>
        <li><svg viewBox="0 0 40 40"><path d="M6 20 L16 30 L34 8" fill="none" stroke="var(--gold)" stroke-width="7" stroke-linejoin="round"/></svg><b>QUICK TURNAROUND</b> - FAST AND EFFICIENT SERVICE</li>
      </ul>
      <div class="brand">OLUM ROOFING</div>
      <div class="site">OLUMROOFING.COM</div>
      <div class="phone">877.612.OLUM</div>
    </section>
  </div>

</main>
</body>
</html>
```